High end, luxury real estate property brochure

I need to have a property Brochure with 10-15 pages that will allow me to enter 30-40 photos and content about the home. It needs to be very high end and able to be edited in either word or publisher. I want to be able to use the pages individually when appropriate and then all together for larger homes. I need the template back by early Wednesday morning. Ideally, the brochure will be like a small booklet with a place for photos and content on the front and back of the pages. I need to add my company's logo and my photo to the project along with our office address etc..
Updates

Project Deadline Extended
Reason: I have decided to purchase more than one design and want to extend time for additional submissions.

Target Market(s)

Home Buyers in the Midwest (Indiana)

Industry/Entity Type

Real Estate Agent

Font styles to use
Serif

Requirements
Must have
• Graphically appealing. Integrated look between the pages. Several places for me to add photos of different sizes to highlight the homes features. The ability for me to change font, font colors, background colors, etc... Must have a high end, luxury feel. I will be adding descriptions and content about the photos so I need areas to add that information. I want the project to be able to be printed as a booklet for larger homes and to be able to use parts of the brochure for smaller homes as I won't have as many photos. Resolution must be fantastic. Clean lines.
Nice to have
• I am with Brandt Okafor Realty and our colors our logo is red so many of our publications are in Black and red. Dorian Pratt Promo Studios is a program that has some high end marketing pieces and designs that I like. I prefer the designs in the slate and black colors.
Should not have
• Cartoons graphics, pastel colors, "busy" designs.

```html
<!DOCTYPE html>
<html lang="en">
<head>
<meta charset="utf-8">
<title>Brandt Okafor Realty – Property Brochure Spread</title>
<link rel="stylesheet" href="https://fonts.googleapis.com/css2?family=Montserrat:wght@400;600;700&display=swap">
<style>
  :root {
    --canvas: #ececec;
    --page: #000000;
    --header: #ffffff;
    --brand-red: #c8102e;
    --ink: #1a1a1a;
    --slate: #5a5a5a;
    --slate-text: #f2f2f2;
    --gutter: #2a2a2a;
  }
  * { box-sizing: border-box; margin: 0; padding: 0; }
  html, body {
    width: 1200px; height: 941px; overflow: hidden;
    background: var(--canvas);
    font-family: "Montserrat", sans-serif;
  }
  .spread {
    position: absolute; left: 0; top: 46px;
    width: 1200px; height: 848px;
    display: flex;
  }
  .page {
    position: relative;
    width: 600px; height: 848px;
    background: var(--page);
  }
  .page + .page { border-left: 2px solid var(--gutter); }

  .page-header {
    position: absolute; left: 37px; top: 35px;
    width: 526px; height: 37px;
    background: var(--header);
    display: flex; align-items: center; justify-content: space-between;
    padding: 0 18px 0 190px;
  }
  .page-header::after {
    content: ""; position: absolute;
    left: 250px; top: 37px;
    border-left: 13px solid transparent;
    border-right: 13px solid transparent;
    border-top: 13px solid var(--header);
    z-index: 2;
  }
  .brand-name {
    color: var(--brand-red);
    font-weight: 700; font-size: 15px; letter-spacing: 0.02em;
  }
  .contact {
    display: flex; align-items: center; gap: 6px;
    color: var(--ink); font-weight: 600; font-size: 11px;
  }

  .photo { position: absolute; }
  .slate-box {
    position: absolute;
    background: var(--slate);
    color: var(--slate-text);
    padding: 14px 14px;
    font-size: 9.5px; line-height: 1.55;
  }
  .slate-box h3 {
    font-size: 9px; font-weight: 700; margin-bottom: 4px; letter-spacing: 0.03em;
  }
  .slate-box ul { list-style: none; margin-bottom: 14px; }
  .slate-box li::before { content: "• "; }

  /* left page */
  .hero-modern { left: 37px; top: 72px; width: 526px; height: 305px;
    background: linear-gradient(180deg, #3b6fa6 0%, #6d8fb0 45%, #d7d7d2 70%, #1d3d6e 100%); }
  .living-a { left: 37px; top: 382px; width: 198px; height: 140px;
    background: linear-gradient(160deg, #c9c6c0, #7c766c); }
  .living-b { left: 37px; top: 527px; width: 198px; height: 140px;
    background: linear-gradient(160deg, #e8e3da, #8d6e4f); }
  .kitchen { left: 37px; top: 672px; width: 198px; height: 139px;
    background: linear-gradient(160deg, #d4d2cd, #6e6a64); }
  .dusk-facade { left: 240px; top: 382px; width: 323px; height: 158px;
    background: linear-gradient(180deg, #1f3f78 0%, #2c528c 55%, #e2a24a 75%, #18233a 100%); }
  .features-box { left: 240px; top: 545px; width: 323px; height: 266px; padding-top: 24px; }

  /* right page */
  .hero-estate { left: 37px; top: 72px; width: 526px; height: 354px;
    background: linear-gradient(180deg, #d49a86 0%, #5e6b3b 35%, #3e4a2a 60%, #6f6650 80%, #2c3324 100%); }
  .description-box { left: 37px; top: 431px; width: 526px; height: 137px; }
  .gallery {
    position: absolute; left: 37px; top: 573px;
    width: 526px; height: 238px;
    display: grid; grid-template-columns: repeat(3, 1fr); grid-template-rows: repeat(2, 1fr);
    gap: 5px;
  }
  .gallery .tile { position: static; }
  .tile-1 { background: linear-gradient(160deg, #8a7a4e, #3d3a22); }
  .tile-2 { background: linear-gradient(160deg, #b06a35, #4a2a16); }
  .tile-3 { background: linear-gradient(160deg, #c99a6a, #6b4a2c); }
  .tile-4 { background: linear-gradient(160deg, #4f5a3a, #2a2f1e); }
  .tile-5 { background: linear-gradient(160deg, #a8743e, #3d2613); }
  .tile-6 { background: linear-gradient(160deg, #d2a26e, #7a5432); }
</style>
</head>
<body>
  <main class="spread">
    <section class="page page-left">
      <header class="page-header">
        <span class="brand-name">Brandt Okafor Realty</span>
        <span class="contact">
          <svg width="12" height="12" viewBox="0 0 24 24" aria-hidden="true"><circle cx="12" cy="12" r="11" fill="none" stroke="#1a1a1a" stroke-width="2"/><path d="M8 6l2 0 1 3-1.5 1.2a8 8 0 0 0 4.3 4.3L15 13l3 1v2c0 1-1 2-2 2A10 10 0 0 1 6 8c0-1 1-2 2-2z" fill="#1a1a1a"/></svg>
          317 555 0148
        </span>
      </header>
      <div class="photo hero-modern" role="img" aria-label="Photo of a white contemporary home at dusk with a lit pool and stepping stones"></div>
      <div class="photo living-a" role="img" aria-label="Photo of a bright open living room"></div>
      <div class="photo living-b" role="img" aria-label="Photo of a lounge with warm lighting"></div>
      <div class="photo kitchen" role="img" aria-label="Photo of a modern kitchen with island"></div>
      <div class="photo dusk-facade" role="img" aria-label="Photo of the home's glass facade lit at twilight"></div>
      <div class="slate-box features-box">
        <h3>Property features</h3>
        <ul>
          <li>5,200 Square Feet Interior</li>
          <li>1.4 Acre Lot</li>
        </ul>
        <h3>Property description</h3>
        <p>Set on a quiet wooded lane, this contemporary residence pairs walls of glass with crisp white stone. Open living spaces flow to a lit pool terrace, while the chef's kitchen, wine room and primary suite offer calm, refined comfort year round.</p>
      </div>
    </section>

    <section class="page page-right">
      <header class="page-header">
        <span class="brand-name">Brandt Okafor Realty</span>
        <span class="contact">
          <svg width="12" height="12" viewBox="0 0 24 24" aria-hidden="true"><circle cx="12" cy="12" r="11" fill="none" stroke="#1a1a1a" stroke-width="2"/><path d="M8 6l2 0 1 3-1.5 1.2a8 8 0 0 0 4.3 4.3L15 13l3 1v2c0 1-1 2-2 2A10 10 0 0 1 6 8c0-1 1-2 2-2z" fill="#1a1a1a"/></svg>
          317 555 0148
        </span>
      </header>
      <div class="photo hero-estate" role="img" aria-label="Photo of a timber and brick estate at sunset behind a stone water garden"></div>
      <div class="slate-box description-box">
        <h3>Property description</h3>
        <p>Nestled among mature oaks and a stone water garden, this storybook estate blends timber, brick and warm light. Grand rooms with beamed ceilings open to terraces, a koi pond and evening fire pit, creating a private retreat for gatherings large and small.</p>
      </div>
      <div class="gallery">
        <div class="photo tile tile-1" role="img" aria-label="Photo of an arched entry hall"></div>
        <div class="photo tile tile-2" role="img" aria-label="Photo of a wood-panelled family room"></div>
        <div class="photo tile tile-3" role="img" aria-label="Photo of a beamed dining room"></div>
        <div class="photo tile tile-4" role="img" aria-label="Photo of the wooded garden grounds"></div>
        <div class="photo tile tile-5" role="img" aria-label="Photo of a library lounge"></div>
        <div class="photo tile tile-6" role="img" aria-label="Photo of a sunlit great room"></div>
      </div>
    </section>
  </main>
</body>
</html>
```